Introduction brochure for IT Company

We need a brochure for introducing our new small business services to the market.

We need a template that we can alter and play with as services change, and was thinking about the following:

A front page which has logo (attached), and follows colour scheme used on our website www.qexdatalink.com.au, that has a small description of the service/or us, we are introducing and Call us on 1300 871 629 at the bottom of page.
For the first print only front page and back page will be used, as we are still refining the service. We will be introducing the company to new prospects face to face and want to leave them with a small brochure which explains what we do for them, and clear contact details.

Middle section we have not worked out fully yet, as it depends on space available, but please use points under service on our website for now to fill in with some points.

Last page we want to have the last 1/3 of page to be our contact details along with a google map of our location etc. like the contact us page on website.

We prefer to stay on the lighter side, so more playful in style but you guys are the experts.

Target Market(s)

Small business 1-10 Employees

Industry/Entity Type

It Company

Font styles to use
Serif

Requirements
Must have
• Clear contact details, playful design which is easy to read. Follow colour scheme or close to website, www.qexdatalink.com.au, as this is reflected in all our marketing. Some artistic license is of course given.
Nice to have
• Nothing comes to mind, go crazy and make it fun.
Should not have
• typical images of large scale server racks and enterprise level images. Stay small business.

```html
<!DOCTYPE html>
<html lang="en">
<head>
<meta charset="utf-8">
<title>QEX Datalink – Brochure</title>
<link rel="stylesheet" href="https://fonts.googleapis.com/css2?family=Lato:wght@400;700;900&family=Roboto+Condensed:wght@400&display=swap">
<style>
  :root {
    --red: #e3191f;
    --red-deep: #c4121a;
    --red-soft: #ef4a4f;
    --charcoal: #2a2a2a;
    --white: #ffffff;
    --stage: #e9e9ea;
    --map-grey: #e4e4e4;
    --icon-grey: #4a4a4a;
    --photo-a: #d9dde3;
    --photo-b: #b9a79a;
  }
  html, body { margin: 0; padding: 0; overflow: hidden; }
  body { width: 1200px; height: 1200px; background: var(--stage); font-family: "Lato", sans-serif; }
  .spread { position: absolute; left: 80px; top: 232px; width: 1040px; height: 735px; display: flex; box-shadow: 0 18px 40px rgba(0,0,0,.18); }
  .page { position: relative; width: 520px; height: 735px; overflow: hidden; }
  .page-art { position: absolute; left: 0; top: 0; }

  /* back page */
  .contact { position: absolute; left: 258px; top: 500px; width: 255px; color: var(--white); font-size: 13.5px; line-height: 1.45; }
  .contact-title { font-size: 17px; letter-spacing: 1px; margin: 0 0 6px; font-weight: 400; }
  .contact-call { color: var(--red); font-size: 17px; margin: 0 0 4px; }
  .contact p { margin: 0; }
  .contact-web-label { color: var(--red); font-size: 16px; margin-top: 12px !important; }
  .contact-web { color: var(--red); font-size: 16px; font-weight: 700; }
  .ico { display: inline-block; vertical-align: -2px; margin-right: 5px; }

  /* front page */
  .brand { position: absolute; top: 34px; left: 190px; display: flex; align-items: center; gap: 10px; }
  .brand-name { font-family: "Lato", sans-serif; font-weight: 900; font-size: 30px; color: var(--red); letter-spacing: 1px; }
  .brand-dot { width: 16px; height: 16px; border-radius: 50%; background: var(--red); }
  .headline { position: absolute; top: 460px; left: 0; right: 0; text-align: center; }
  .headline-ask { color: var(--red); font-weight: 700; font-size: 28px; letter-spacing: 1.5px; margin: 0; }
  .headline-offer { color: var(--white); font-family: "Roboto Condensed", sans-serif; font-size: 31px; margin: 2px 0 0; }
  .services { position: absolute; top: 560px; left: 0; right: 0; padding: 0 10px; display: flex; justify-content: space-between; }
  .service { width: 122px; text-align: center; font-size: 11.5px; line-height: 1.35; white-space: nowrap; }
  .service-badge { width: 56px; height: 56px; border-radius: 50%; background: var(--icon-grey); margin: 0 auto 8px; display: flex; align-items: center; justify-content: center; }
  .service-kind { color: var(--red); display: block; }
  .service-scope { color: var(--white); display: block; }
</style>
</head>
<body>
<div class="spread">

  <section class="page page-back">
    <svg class="page-art" viewBox="0 0 520 735" width="520" height="735">
      <defs>
        <linearGradient id="backPhoto" x1="0" y1="0" x2="1" y2="1">
          <stop offset="0" stop-color="#e8262c"/>
          <stop offset=".5" stop-color="#f0474c"/>
          <stop offset="1" stop-color="#d5161d"/>
        </linearGradient>
      </defs>
      <rect width="520" height="735" fill="url(#backPhoto)" role="img" aria-label="Red-tinted photo of a hand holding a tablet showing business charts"/>
      <path d="M0,600 C120,470 300,430 520,405 L520,735 L0,735 Z" fill="var(--white)"/>
      <path d="M0,612 C120,484 300,442 520,416 L520,735 L0,735 Z" fill="var(--red)"/>
      <path d="M0,620 C120,492 300,450 520,424 L520,735 L0,735 Z" fill="var(--charcoal)"/>
      <circle cx="118" cy="628" r="122" fill="var(--white)"/>
      <circle cx="118" cy="628" r="114" fill="var(--map-grey)" stroke="var(--red)" stroke-width="3" role="img" aria-label="Street map showing the office location"/>
    </svg>
    <div class="contact">
      <h2 class="contact-title">CONTACT INFO</h2>
      <p class="contact-call"><svg class="ico" width="13" height="13" viewBox="0 0 24 24"><path d="M6.6 10.8a15.2 15.2 0 006.6 6.6l2.2-2.2c.3-.3.7-.4 1-.2 1.1.4 2.3.6 3.6.6.6 0 1 .4 1 1V20c0 .6-.4 1-1 1A17 17 0 013 4c0-.6.4-1 1-1h3.5c.6 0 1 .4 1 1 0 1.3.2 2.5.6 3.6.1.3 0 .7-.2 1z" fill="var(--red)"/></svg>Call us on: 1300 871 629</p>
      <p>Email: service@qexdatalink.com.au</p>
      <p><svg class="ico" width="11" height="14" viewBox="0 0 24 30"><path d="M12 0C5.4 0 0 5.4 0 12c0 9 12 18 12 18s12-9 12-18C24 5.4 18.6 0 12 0zm0 16a4 4 0 110-8 4 4 0 010 8z" fill="var(--red)"/></svg>Address: 4/18 Harlow Street,</p>
      <p>Kingsmere TAS 7021</p>
      <p>Hours: Monday-Friday 9am - 5pm</p>
      <p class="contact-web-label">Visit our Website</p>
      <p class="contact-web">www.qexdatalink.com.au</p>
    </div>
  </section>

  <section class="page page-front">
    <svg class="page-art" viewBox="0 0 520 735" width="520" height="735">
      <defs>
        <linearGradient id="frontPhoto" x1="0" y1="0" x2="1" y2="1">
          <stop offset="0" stop-color="var(--photo-a)"/>
          <stop offset="1" stop-color="var(--photo-b)"/>
        </linearGradient>
      </defs>
      <rect width="520" height="735" fill="var(--white)"/>
      <path d="M110,100 L520,100 L520,418 L400,418 C310,404 270,340 175,282 C115,244 98,175 110,100 Z" fill="url(#frontPhoto)" role="img" aria-label="Photo of a family smiling together around a laptop on a sofa"/>
      <path d="M0,0 L72,0 C12,90 30,200 140,270 C260,345 300,408 390,422 L520,422 L520,445 L0,445 Z" fill="var(--white)"/>
      <path d="M0,0 L62,0 C4,92 22,205 132,276 C252,352 292,414 385,430 L520,430 L520,445 L0,445 Z" fill="var(--red)"/>
      <path d="M0,0 L52,0 C-2,95 14,210 124,282 C244,358 284,420 380,436 L520,436 L520,445 L0,445 Z" fill="var(--red-soft)"/>
      <rect y="443" width="520" height="292" fill="var(--charcoal)"/>
    </svg>
    <div class="brand"><span class="brand-name">QEX DATALINK</span><span class="brand-dot"></span></div>
    <div class="headline">
      <p class="headline-ask">NEED SOME HELP?</p>
      <p class="headline-offer">WE OFFER SEVERAL OPTIONS</p>
    </div>
    <div class="services">
      <div class="service">
        <div class="service-badge"><svg width="30" height="28" viewBox="0 0 30 28"><path d="M15 2 L28 13 L24 13 L24 26 L6 26 L6 13 L2 13 Z" fill="#f2f2f2"/><rect x="12" y="17" width="6" height="9" fill="var(--icon-grey)"/></svg></div>
        <span class="service-kind">Residential computer /</span><span class="service-scope">network issues</span>
      </div>
      <div class="service">
        <div class="service-badge"><svg width="32" height="26" viewBox="0 0 32 26"><path d="M9 14a6 6 0 01.6-12 8 8 0 0114.6 3A5 5 0 0124 14z" fill="#5aa9e6"/><rect x="3" y="18" width="8" height="6" fill="#5aa9e6"/><rect x="21" y="18" width="8" height="6" fill="#5aa9e6"/><path d="M16 14v3M7 18v-1h18v1" stroke="#5aa9e6" stroke-width="1.5" fill="none"/></svg></div>
        <span class="service-kind">Business computer /</span><span class="service-scope">network issues</span>
      </div>
      <div class="service">
        <div class="service-badge"><svg width="32" height="26" viewBox="0 0 32 26"><rect x="2" y="3" width="28" height="17" rx="2" fill="#f2f2f2"/><rect x="5" y="6" width="22" height="11" fill="#4d8fd6"/><rect x="12" y="21" width="8" height="3" fill="#f2f2f2"/></svg></div>
        <span class="service-kind">Home</span><span class="service-scope">Networking</span>
      </div>
      <div class="service">
        <div class="service-badge"><svg width="30" height="28" viewBox="0 0 30 28"><path d="M15 2 L28 13 L24 13 L24 26 L6 26 L6 13 L2 13 Z" fill="#f2f2f2"/><circle cx="15" cy="18" r="5" fill="#4d8fd6"/></svg></div>
        <span class="service-kind">New Home</span><span class="service-scope">Networking</span>
      </div>
    </div>
  </section>

</div>
</body>
</html>
```